Website redesign for a Cloud Advisory business

We are looking to revisit our existing brand and website, with a view to updating both. Looking for concepts and designs for how the website might look, flow and feel. Current website is: www.brightlane.com.au

Scope and Deliverables: Concept design for the home page and one internal page.

We do not expect you to design all the pages and all the elements of the website at this stage.

This job is not for the full website design, but just for concepts that we can start with when we go into the full website design.

We would love to see a design feature based on our name, logo, or industry, which can run through banners and other collateral (chirpnet banner, ads on Findora, corporate documents etc).

We want the brand to properly depict what we bring/deliver to businesses when consulting to them and this should extend to the colour scheme, logo, font (perhaps updated) and copy (which will be supplied).

Our brand should suitably communicate our ability, knowledge and extensive experience within the Cloud space.

It should express and evoke credibility, knowledge and understanding of the Cloud space, independence, gravitas, reliability, efficiency, trust, expertise, approachability, service delivery but be uncomplicated, practical and use plain speaking language.

Colours that reinforce this might include: Blues, blacks, silver, white, grey and our existing orange.

Website designs that we like or have referenced include:

Skyvault: http://skyvault.com.au/ - This has good information but looks a little amateur in it’s cartoon like design and colour scheme. Also, this seems to be aimed at clients more interested in price than design and what we are going for is a little more high end.

Nimbuspath: https://www.nimbuspath.com.au/ - This site has merit in its’ setup but little call to action on the home page, especially before the scroll line. I like the set up of the Case Studies page however I’d look to make it more prominent by having it set up 3 across rather than the 4 they have. Something such as this: https://www.tallyrig.com/case-studies

Pelwyn: http://www.pelwyn.com.au/#home4 - This page is a good one as far as selling services and information on the company. I quite like it.

BorealIT: http://www.borealit.com.au/ - While I don’t think is particularly creative, it does practically depict the services we offer in a fairly clear way and might be a bit of a basic (albeit dull) template to follow.

QRV: https://store.qrv.com/us/Product-Family/QRV-Advisory-Services/QRV-Cloud-Advisory-Service/p/QRV-Services-Cloud-Advisory - This offers substantial information but is probably a little confusing although the roll-over drop down menus have merit.

LUP: http://www.lup.net.au/en/services/ - While this in not quite what we are looking for, the colour scheme gives it more gravitas and quality.

As another reference, this website and the way they present their case studies is also something we like, although I’d like them shown 3 up, side by side…. https://www.tallyrig.com/case-studies.

We have added a page layout and page purpose document.

Target Market(s)

Corporates, small - medium business, direct referrals, via search results

Industry/Entity Type

Business

Number of Pages Required

1 page

Font styles to use
Sans Serif

Colors
85abd2
0455a3
000000
f37122
5c5c5c

Requirements
Must have
• Website must be mobile device compatible.
• Concept design for the home page.
Nice to have
• We would love to see a design feature based on our name, logo, or industry, which can run through banners and other collateral (chirpnet banner, ads on Findora, corporate documents etc).

```html
<!DOCTYPE html>
<html lang="en">
<head>
<meta charset="utf-8">
<title>Brightlane — Impartial Cloud Solutions</title>
<link rel="stylesheet" href="https://fonts.googleapis.com/css2?family=Open+Sans:wght@400;600;700&family=Roboto+Slab:wght@400;700&display=swap">
<style>
  :root {
    --orange: #f37122;
    --orange-dark: #d95e14;
    --ink: #1e1e1e;
    --grey: #5c5c5c;
    --grey-light: #9a9a9a;
    --line: #e3e3e3;
    --white: #ffffff;
    --hero-top: #2a5d9c;
    --hero-bottom: #8fb3da;
    --arrow-bg: rgba(20, 30, 45, 0.75);
    --slab: "Roboto Slab", Georgia, serif;
    --sans: "Open Sans", Arial, sans-serif;
  }
  * { box-sizing: border-box; margin: 0; padding: 0; }
  html, body { width: 1200px; height: 600px; overflow: hidden; background: var(--white); }
  body { font-family: var(--sans); color: var(--ink); }

  .site-header { height: 72px; border-bottom: 1px solid var(--line); }
  .header-inner {
    width: 1000px; margin: 0 auto; height: 100%;
    display: flex; align-items: center; justify-content: space-between;
  }
  .brand { display: flex; align-items: center; gap: 10px; }
  .brand-square { width: 22px; height: 22px; background: var(--orange); }
  .brand-name { font-family: var(--sans); font-weight: 700; font-size: 26px; letter-spacing: 1px; color: var(--ink); }
  .header-right { display: flex; flex-direction: column; align-items: flex-end; gap: 8px; }
  .search-box {
    width: 170px; height: 20px; border: 1px solid var(--line);
    font-size: 10px; color: var(--grey-light); padding: 3px 8px;
  }
  .main-nav { display: flex; gap: 26px; font-size: 12px; color: var(--grey); }
  .main-nav .is-active { color: var(--orange); font-weight: 600; border-bottom: 2px solid var(--orange); padding-bottom: 2px; }

  .sub-nav { height: 30px; background: var(--orange); }
  .sub-nav-inner {
    width: 1000px; margin: 0 auto; height: 100%;
    display: flex; align-items: center; gap: 42px;
    font-family: var(--slab); font-size: 13px; color: var(--white);
  }

  .hero { position: relative; height: 330px; overflow: hidden; }
  .hero-visual {
    position: absolute; inset: 0;
    background: linear-gradient(180deg, var(--hero-top) 0%, var(--hero-bottom) 100%);
  }
  .hero-content { position: relative; width: 1000px; margin: 0 auto; padding-top: 58px; color: var(--white); }
  .hero-title { font-family: var(--slab); font-weight: 400; font-size: 46px; line-height: 1.12; }
  .hero-lead { font-size: 17px; font-weight: 600; margin-top: 14px; max-width: 470px; line-height: 1.35; }
  .hero-note { font-size: 11px; margin-top: 10px; max-width: 440px; opacity: 0.9; }
  .cta-button {
    display: inline-flex; align-items: center; gap: 8px; margin-top: 20px;
    background: var(--orange); color: var(--white);
    font-size: 10px; font-weight: 700; letter-spacing: 0.5px;
    padding: 9px 16px; border-bottom: 2px solid var(--orange-dark);
  }
  .cta-dot { width: 8px; height: 8px; border-radius: 50%; background: var(--white); }
  .slider-arrow {
    position: absolute; top: 146px; width: 26px; height: 34px;
    background: var(--arrow-bg); display: flex; align-items: center; justify-content: center;
  }
  .slider-arrow.prev { left: 0; }
  .slider-arrow.next { right: 0; }

  .services { height: 168px; }
  .services-inner {
    width: 1000px; margin: 0 auto; padding-top: 26px;
    display: grid; grid-template-columns: repeat(3, 1fr); gap: 40px;
  }
  .service-title { display: flex; align-items: center; gap: 10px; font-family: var(--slab); font-size: 15px; color: var(--ink); }
  .service-icon {
    width: 26px; height: 26px; border-radius: 50%; background: var(--orange);
    display: flex; align-items: center; justify-content: center; flex: none;
  }
  .service-text { font-size: 11px; line-height: 1.55; color: var(--grey); margin-top: 10px; }
  .learn-more { display: block; text-align: right; font-size: 10px; color: var(--ink); font-weight: 600; margin-top: 10px; }
  .learn-more span { color: var(--orange); }
</style>
</head>
<body>
  <header class="site-header">
    <div class="header-inner">
      <div class="brand">
        <span class="brand-square"></span>
        <span class="brand-name">BRIGHTLANE</span>
      </div>
      <div class="header-right">
        <div class="search-box">Search ...</div>
        <nav class="main-nav">
          <span class="is-active">Home</span>
          <span>About Us</span>
          <span>Solutions</span>
          <span>FAQ's</span>
          <span>Blog</span>
          <span>Contact Us</span>
        </nav>
      </div>
    </div>
  </header>

  <nav class="sub-nav">
    <div class="sub-nav-inner">
      <span>Industry Specialties</span>
      <span>The Company We Keep</span>
      <span>Case Studies &amp; Testimonials</span>
      <span>Resources &amp; Links</span>
    </div>
  </nav>

  <section class="hero">
    <div class="hero-visual" role="img" aria-label="Photo of a businessman with a laptop standing on a rock under a blue sky with white clouds"></div>
    <div class="hero-content">
      <h1 class="hero-title">Impartial<br>Cloud Solutions</h1>
      <p class="hero-lead">We provide impartial advice on cloud solutions ensuring it's always right for you.</p>
      <p class="hero-note">Clear, vendor-neutral guidance for every stage of your move to the cloud.</p>
      <span class="cta-button"><span class="cta-dot"></span>BOOK A FREE CONSULTATION</span>
    </div>
    <span class="slider-arrow prev">
      <svg width="10" height="14" viewBox="0 0 10 14"><path d="M8 1 L2 7 L8 13" fill="none" stroke="#fff" stroke-width="2"/></svg>
    </span>
    <span class="slider-arrow next">
      <svg width="10" height="14" viewBox="0 0 10 14"><path d="M2 1 L8 7 L2 13" fill="none" stroke="#fff" stroke-width="2"/></svg>
    </span>
  </section>

  <section class="services">
    <div class="services-inner">
      <article class="service">
        <h2 class="service-title">
          <span class="service-icon"><svg width="12" height="12" viewBox="0 0 12 12"><path d="M2 6 L5 9 L10 3" fill="none" stroke="#fff" stroke-width="2"/></svg></span>
          System Selection
        </h2>
        <p class="service-text">We compare platforms side by side and match each option to your processes, budget and growth plans before you commit.</p>
        <span class="learn-more">Learn More <span>›</span></span>
      </article>
      <article class="service">
        <h2 class="service-title">
          <span class="service-icon"><svg width="12" height="12" viewBox="0 0 12 12"><rect x="1" y="3" width="10" height="6" fill="none" stroke="#fff" stroke-width="1.6"/></svg></span>
          Integration
        </h2>
        <p class="service-text">We connect new cloud tools with the systems you already run so data flows cleanly and teams keep working without disruption.</p>
        <span class="learn-more">Learn More <span>›</span></span>
      </article>
      <article class="service">
        <h2 class="service-title">
          <span class="service-icon"><svg width="12" height="12" viewBox="0 0 12 12"><circle cx="6" cy="5" r="3" fill="#fff"/><path d="M6 8 L6 11" stroke="#fff" stroke-width="1.6"/></svg></span>
          Business Inventory
        </h2>
        <p class="service-text">We map the software, licences and services across your business so you know exactly what you own and what it costs.</p>
        <span class="learn-more">Learn More <span>›</span></span>
      </article>
    </div>
  </section>
</body>
</html>
```